Lucien Dorval

Changes to attached business card: 1. Eliminate borders (black) top and bottom of the existing card. 2- eliminate: Become the reference! 3- adding: www.boostezvoschiffres.ca info@boostezvoschiffres.ca luciendorvalconseil.com (819) 555-2731 4- black on white

Contact Information for Business Card

voir pièce ci-jointe pour exemple

Requirements
Must have
• black on white
Nice to have
• Very modern ! with punch!

```html
<!DOCTYPE html>
<html lang="fr">
<head>
<meta charset="utf-8">
<title>Lucien Dorval – Carte professionnelle</title>
<link rel="stylesheet" href="https://fonts.googleapis.com/css2?family=Lato:wght@400;700&display=swap">
<style>
  :root {
    --bg: #ffffff;
    --panel: #f0f0f0;
    --frame: #111111;
    --ink: #111111;
    --photo-light: #f4f1ee;
    --photo-dark: #2a2a30;
  }
  * { margin: 0; padding: 0; box-sizing: border-box; }
  html, body { width: 1200px; height: 720px; overflow: hidden; background: var(--bg); }
  .card {
    position: relative;
    width: 1200px; height: 720px;
    background: var(--bg);
    color: var(--ink);
    font-family: "Lato", sans-serif;
  }

  /* Identity block */
  .identity {
    position: absolute; left: 80px; top: 172px; width: 490px;
    text-align: center;
  }
  .identity__name {
    font-weight: 700;
    font-size: 52px; line-height: 1; letter-spacing: 2px;
    text-transform: uppercase;
    color: var(--ink);
  }
  .identity__role {
    display: flex; align-items: center; justify-content: center; gap: 10px;
    margin-top: 10px;
    font-size: 24px; font-weight: 700; line-height: 1;
  }
  .identity__role::before, .identity__role::after {
    content: ""; height: 2px; width: 100px; background: var(--ink);
  }
  .divider {
    position: absolute; left: 95px; top: 309px;
    width: 463px; height: 2px; background: var(--ink);
  }

  /* Contact list */
  .contacts {
    position: absolute; left: 92px; top: 344px;
    list-style: none;
  }
  .contacts__item {
    display: flex; align-items: center;
    height: 58.5px;
    font-size: 30px; color: var(--ink);
  }
  .contacts__icon {
    width: 30px; height: 30px; margin-right: 22px; flex: none;
  }

  /* Portrait panel */
  .portrait-panel {
    position: absolute; left: 669px; top: -20px;
    width: 393px; height: 579px;
    background: var(--panel);
    border-radius: 0 0 44px 44px;
    box-shadow: 0 4px 10px rgba(0,0,0,0.15);
  }
  .portrait-frame {
    position: absolute; left: 18px; top: 121px;
    width: 357px; height: 358px;
    background: var(--frame);
    padding: 13px;
  }
  .portrait-photo {
    width: 100%; height: 100%;
    background: linear-gradient(to bottom, var(--photo-light) 0%, #d9cbc2 55%, var(--photo-dark) 100%);
  }
  .portrait-name {
    position: absolute; left: 0; right: 0; top: 493px;
    text-align: center;
    font-size: 40px; line-height: 1; color: var(--ink);
  }
  .portrait-name__first { font-weight: 700; }
  .portrait-name__last { font-weight: 400; }
</style>
</head>
<body>
<main class="card">
  <header class="identity">
    <div class="identity__name">Lucien Dorval</div>
    <div class="identity__role">Consultant - Coach</div>
  </header>
  <div class="divider"></div>

  <ul class="contacts">
    <li class="contacts__item">
      <svg class="contacts__icon" viewBox="0 0 30 30" aria-hidden="true">
        <path d="M3 11 C3 6 27 6 27 11 L27 13 L21 13 L21 10 L9 10 L9 13 L3 13 Z" fill="#111"/>
        <path d="M9 13 L21 13 L25 23 L5 23 Z" fill="#111"/>
        <circle cx="15" cy="18" r="3" fill="#fff"/>
      </svg>
      <span>(819) 555-2731</span>
    </li>
    <li class="contacts__item">
      <svg class="contacts__icon" viewBox="0 0 30 30" aria-hidden="true">
        <rect x="2" y="7" width="26" height="17" fill="none" stroke="#111" stroke-width="2"/>
        <path d="M2 7 L15 17 L28 7 M2 24 L12 15 M28 24 L18 15" fill="none" stroke="#111" stroke-width="2"/>
      </svg>
      <span>info@boostezvoschiffres.ca</span>
    </li>
    <li class="contacts__item">
      <svg class="contacts__icon" viewBox="0 0 30 30" aria-hidden="true">
        <g fill="none" stroke="#111" stroke-width="1.8">
          <circle cx="15" cy="15" r="12"/>
          <ellipse cx="15" cy="15" rx="5.5" ry="12"/>
          <path d="M3 15 H27 M5 9 H25 M5 21 H25 M15 3 V27"/>
        </g>
      </svg>
      <span>www.boostezvoschiffres.ca</span>
    </li>
    <li class="contacts__item">
      <svg class="contacts__icon" viewBox="0 0 30 30" aria-hidden="true">
        <g fill="none" stroke="#111" stroke-width="1.8">
          <circle cx="15" cy="15" r="12"/>
          <ellipse cx="15" cy="15" rx="5.5" ry="12"/>
          <path d="M3 15 H27 M5 9 H25 M5 21 H25 M15 3 V27"/>
        </g>
      </svg>
      <span>luciendorvalconseil.com</span>
    </li>
  </ul>

  <aside class="portrait-panel">
    <div class="portrait-frame">
      <div class="portrait-photo" role="img" aria-label="Portrait photo of Lucien Dorval in a dark suit on a white background"></div>
    </div>
    <div class="portrait-name"><span class="portrait-name__first">LUCIEN</span> <span class="portrait-name__last">DORVAL</span></div>
  </aside>
</main>
</body>
</html>
```